Illustration Design Project

We need two simple, clean circle illustrations of the Hero's Journey that use our terminology. These will be used for Power Point presentations and other paper support docs as part of our programs that help writers, authors, and thought leaders create and shape their books.

We would like to see designs that
- have a white or off-white background complemented with our branded orange and red
- divided according to the attached illustration into 3 Acts
- move clock wise (not counter-clock wise)

The final design should communicate adventure and courage.

Designers should visit bristle harbor.com to understand the company branding colors and logos.

Target Market(s)

writers, authors, thought leaders, coaches, business people who are writing books

Industry/Entity Type

It Company

Requirements
Must have
• - have a white or off-white background complemented with our branded orange and red
- be super-clean and easy-to-read
Nice to have
• nothing too fancy - but if you have an idea to evoke courage without it being corny, that would be fine
Should not have
• Do not go for cliched "journey"-like images.

```html
<!DOCTYPE html>
<html lang="en">
<head>
<meta charset="UTF-8">
<title>The Hero's Journey in Three Acts</title>
<link rel="stylesheet" href="https://fonts.googleapis.com/css2?family=Roboto:wght@400;700&display=swap">
<style>
  :root {
    --bg: #fffaf2;
    --brand-orange: #f39200;
    --brand-orange-light: #f9b04a;
    --brand-orange-deep: #d97800;
    --brand-red: #cf2a27;
    --brand-red-deep: #a91e1c;
    --act2-tint: #fbd3a0;
    --node-edge: #ffffff;
    --node-soft: #fff6e6;
    --ink: #2a2a2a;
    --horizon: #c9b8a3;
  }
  html, body {
    margin: 0;
    padding: 0;
    width: 1200px;
    height: 900px;
    overflow: hidden;
    background: var(--bg);
  }
  .journey {
    display: block;
    width: 1200px;
    height: 900px;
    font-family: "Roboto", Arial, sans-serif;
  }
  .stage-label {
    font-size: 24px;
    fill: var(--ink);
  }
  .stage-number {
    font-size: 18px;
    font-weight: 700;
    text-anchor: middle;
    dominant-baseline: central;
  }
  .stage-number--light { fill: #ffffff; }
  .stage-number--dark { fill: var(--brand-red-deep); }
  .act-title {
    font-size: 30px;
    font-weight: 700;
    text-anchor: middle;
    dominant-baseline: central;
  }
  .act-title--one { fill: var(--brand-orange-deep); }
  .act-title--two { fill: var(--brand-orange-deep); }
  .act-title--three { fill: var(--brand-red); }
  .world-title {
    font-size: 27px;
    font-weight: 700;
    text-anchor: middle;
  }
  .world-title--ordinary { fill: var(--brand-orange-deep); }
  .world-title--new { fill: var(--brand-red); }
</style>
</head>
<body>
<svg class="journey" viewBox="0 0 1200 900" xmlns="http://www.w3.org/2000/svg">
  <defs>
    <linearGradient id="act1Gradient" x1="0" y1="0" x2="1" y2="1">
      <stop offset="0" stop-color="var(--brand-orange-light)"/>
      <stop offset="1" stop-color="var(--brand-orange)"/>
    </linearGradient>
    <linearGradient id="horizonShade" x1="0" y1="0" x2="1" y2="0">
      <stop offset="0" stop-color="var(--horizon)" stop-opacity="0"/>
      <stop offset="0.25" stop-color="var(--horizon)" stop-opacity="0.6"/>
      <stop offset="0.75" stop-color="var(--horizon)" stop-opacity="0.6"/>
      <stop offset="1" stop-color="var(--horizon)" stop-opacity="0"/>
    </linearGradient>
    <linearGradient id="dividerLine" x1="0" y1="0" x2="1" y2="0">
      <stop offset="0" stop-color="var(--brand-red)" stop-opacity="0"/>
      <stop offset="0.5" stop-color="var(--brand-red)" stop-opacity="0.7"/>
      <stop offset="1" stop-color="var(--brand-red)" stop-opacity="0"/>
    </linearGradient>
    <radialGradient id="nodeOrange" cx="0.4" cy="0.35" r="0.7">
      <stop offset="0" stop-color="#ffc46b"/>
      <stop offset="1" stop-color="var(--brand-orange-deep)"/>
    </radialGradient>
    <radialGradient id="nodeRed" cx="0.4" cy="0.35" r="0.7">
      <stop offset="0" stop-color="#ef6a5f"/>
      <stop offset="1" stop-color="var(--brand-red-deep)"/>
    </radialGradient>
  </defs>

  <g class="horizon">
    <rect x="0" y="440" width="880" height="8" fill="url(#horizonShade)"/>
    <rect x="360" y="469" width="390" height="3" fill="url(#dividerLine)"/>
  </g>

  <g class="act act--two">
    <path d="M856.6 448.3 A312 312 0 0 1 255.7 549" fill="none" stroke="var(--act2-tint)" stroke-width="33"/>
    <polygon points="283.6,537.7 228,560.1 239.8,496.9" fill="var(--act2-tint)"/>
  </g>

  <g class="act act--one">
    <path d="M528.7 120.4 A312 312 0 0 1 852.3 377.8" fill="none" stroke="url(#act1Gradient)" stroke-width="33"/>
    <polygon points="822.8,383 881.9,372.6 857,426.6" fill="var(--brand-orange)"/>
  </g>

  <g class="act act--three">
    <path d="M233 432 A312 312 0 0 1 464.3 130.6" fill="none" stroke="var(--brand-red)" stroke-width="33"/>
    <polygon points="472,159.6 456.5,101.6 512.4,121.7" fill="var(--brand-red)"/>
  </g>

  <text class="act-title act-title--one" transform="translate(694 212) rotate(36)">ACT 1</text>
  <text class="act-title act-title--two" x="546" y="680">ACT 2</text>
  <text class="act-title act-title--three" transform="translate(358 244) rotate(-48)">ACT 3</text>

  <text class="world-title world-title--ordinary" x="551" y="455">The Ordinary World</text>
  <text class="world-title world-title--new" x="551" y="505">The New World</text>

  <g class="stages">
    <circle cx="550.5" cy="120" r="17" fill="url(#nodeOrange)" stroke="var(--node-edge)" stroke-width="2"/>
    <text class="stage-number stage-number--light" x="550.5" y="120">1</text>
    <circle cx="688.5" cy="155" r="17" fill="url(#nodeOrange)" stroke="var(--node-edge)" stroke-width="2"/>
    <text class="stage-number stage-number--light" x="688.5" y="155">2</text>
    <circle cx="787.5" cy="235.7" r="17" fill="url(#nodeOrange)" stroke="var(--node-edge)" stroke-width="2"/>
    <text class="stage-number stage-number--light" x="787.5" y="235.7">3</text>
    <circle cx="845" cy="346" r="17" fill="url(#nodeOrange)" stroke="var(--node-edge)" stroke-width="2"/>
    <text class="stage-number stage-number--light" x="845" y="346">4</text>

    <circle cx="856" cy="489.4" r="17" fill="var(--node-soft)" stroke="var(--brand-orange)" stroke-width="2.5"/>
    <text class="stage-number stage-number--dark" x="856" y="489.4">5</text>
    <circle cx="806.7" cy="602" r="17" fill="var(--node-soft)" stroke="var(--brand-orange)" stroke-width="2.5"/>
    <text class="stage-number stage-number--dark" x="806.7" y="602">6</text>
    <circle cx="724" cy="687.5" r="17" fill="var(--node-soft)" stroke="var(--brand-orange)" stroke-width="2.5"/>
    <text class="stage-number stage-number--dark" x="724" y="687.5">7</text>
    <circle cx="545" cy="744" r="17" fill="var(--node-soft)" stroke="var(--brand-orange)" stroke-width="2.5"/>
    <text class="stage-number stage-number--dark" x="545" y="744">8</text>
    <circle cx="317" cy="645" r="17" fill="var(--node-soft)" stroke="var(--brand-orange)" stroke-width="2.5"/>
    <text class="stage-number stage-number--dark" x="317" y="645">9</text>

    <circle cx="237" cy="445.6" r="17" fill="url(#nodeRed)" stroke="var(--node-edge)" stroke-width="2"/>
    <text class="stage-number stage-number--light" x="237" y="445.6">10</text>
    <circle cx="268.3" cy="288" r="17" fill="url(#nodeRed)" stroke="var(--node-edge)" stroke-width="2"/>
    <text class="stage-number stage-number--light" x="268.3" y="288">11</text>
    <circle cx="379.6" cy="167.4" r="17" fill="url(#nodeRed)" stroke="var(--node-edge)" stroke-width="2"/>
    <text class="stage-number stage-number--light" x="379.6" y="167.4">12</text>
  </g>

  <g class="labels">
    <text class="stage-label" x="532" y="84">The Ordinary World</text>
    <text class="stage-label" x="741" y="150">The Call to Adventure</text>
    <text class="stage-label" x="832" y="241">Refusal of the Call</text>
    <text class="stage-label" x="897" y="348">Meeting</text>
    <text class="stage-label" x="897" y="382">with Mentor</text>
    <text class="stage-label" x="897" y="494">Crossing the First</text>
    <text class="stage-label" x="897" y="529">Threshold</text>
    <text class="stage-label" x="834" y="615">Test, Allies,</text>
    <text class="stage-label" x="834" y="650">Enemies</text>
    <text class="stage-label" x="720" y="743">Approach to</text>
    <text class="stage-label" x="720" y="777">the Inmost Cave</text>
    <text class="stage-label" x="551" y="804" text-anchor="middle">Supreme Ordeal</text>
    <text class="stage-label" x="202" y="672" text-anchor="middle">Reward</text>
    <text class="stage-label" x="202" y="707" text-anchor="middle">(Seizing the Sword)</text>
    <text class="stage-label" x="207" y="411" text-anchor="end">The Road</text>
    <text class="stage-label" x="207" y="446" text-anchor="end">Back</text>
    <text class="stage-label" x="237" y="300" text-anchor="end">Resurrection</text>
    <text class="stage-label" x="236" y="164" text-anchor="middle">Return with</text>
    <text class="stage-label" x="236" y="198" text-anchor="middle">the Elixir</text>
  </g>
</svg>
</body>
</html>
```